Asia based real estate financing firm needs and AWESOME design for a biz card -Harborline Lending Partners

Looking for a stylish, & corporate-looking business card for a real estate financing brokerage firm in Asia, offering global mortgage loans. I uploaded our current logos. We would like to add a splash of color (perhaps the house icon) or any other suggestions are open. For the winning designer, we have a lot of work! Thanks and best of luck!

Target Market(s)

Real estate investors globally. We want to look more like a BANK and NOT a real estate company. Please don't play up on a "house" design.

Industry/Entity Type

Banking

Contact Information for Business Card

Harborline Lending Partners
Peter Walsh
Co-Founder | Partner

42 Kelvin Street, Suite 310
Singapore 074219
www.hlp-lend.example
peterwalsh@hlp-lend.example
+65 555-0147
WeChat: peterwalsh

Colors

Designer to choose colors to be used in the design.

Requirements
Must have
• Must have the standard business requirements for a card; name, address, email, etc
• Can be horizontal or vertical.
Nice to have
• It would be great to see some sort of variation to the logo with a pop of color. Red is good as we're in Asia, however, other options work as well.
• Our tag line is - Borderless mortgages. It doesn't have to be on the card but might be nice.
• I'd like to start seeing our tagline within the cards as well. - Borderless mortgages.
• Also, please add our location. The location for this card is Singapore so perhaps it can be highlighted or emphasised in some way.
• Singapore | Hong Kong | Shanghai | Manila
• As we will soon open an office in Shanghai, having an option for both languages would be great.
Should not have
• I'm exceited and open to your creativity ... knock it out of the park!

```html
<!DOCTYPE html>
<html lang="en">
<head>
<meta charset="utf-8">
<title>Harborline Lending Partners – Business Card</title>
<link rel="stylesheet" href="https://fonts.googleapis.com/css2?family=Cinzel:wght@500;700&family=Open+Sans:wght@400&display=swap">
<style>
  :root {
    --stage: #333333;
    --card-light: #f3f3f3;
    --brand-blue: #135cb3;
    --ink: #232323;
    --on-blue: #ffffff;
    --shadow: rgba(0, 0, 0, 0.45);
  }
  * { margin: 0; padding: 0; box-sizing: border-box; }
  html, body { width: 1200px; height: 900px; overflow: hidden; }
  body { background: var(--stage); position: relative; font-family: "Open Sans", Arial, sans-serif; }

  .card {
    position: absolute;
    top: 200px;
    width: 310px;
    height: 502px;
    box-shadow: 3px 4px 6px var(--shadow);
  }
  .card--front {
    left: 253px;
    background: var(--card-light);
    border-radius: 62px 0 62px 0;
  }
  .card--back {
    left: 627px;
    background: var(--brand-blue);
    border-radius: 0 62px 0 62px;
  }

  .wordmark {
    position: absolute;
    left: 0;
    width: 100%;
    text-align: center;
    font-family: "Cinzel", Georgia, serif;
    font-weight: 500;
    font-size: 27px;
    line-height: 1.25;
  }
  .wordmark__mark {
    display: block;
    width: 20px;
    height: 20px;
    margin: 0 auto 14px;
  }
  .card--front .wordmark { top: 96px; color: var(--brand-blue); }
  .card--front .wordmark__mark { background: var(--brand-blue); }
  .card--back .wordmark { top: 190px; color: var(--on-blue); }
  .card--back .wordmark__mark { background: var(--on-blue); }

  .contact {
    position: absolute;
    left: 33px;
    top: 300px;
    color: var(--ink);
    font-size: 14.5px;
    line-height: 18px;
  }
  .contact__name {
    font-family: "Cinzel", Georgia, serif;
    font-weight: 700;
    font-size: 21px;
    line-height: 26px;
    color: var(--brand-blue);
  }
  .contact__role { font-size: 14.5px; margin-bottom: 8px; }
  .contact__list { list-style: none; }
  .contact__item { display: flex; align-items: center; gap: 5px; }
  .contact__icon { width: 13px; height: 13px; fill: var(--brand-blue); flex: none; }
  .contact__address { margin-top: 7px; font-style: normal; }
</style>
</head>
<body>
  <section class="card card--front" aria-label="Card front">
    <div class="wordmark">
      <span class="wordmark__mark"></span>
      Harborline<br>Lending Partners
    </div>

    <div class="contact">
      <h1 class="contact__name">PETER WALSH</h1>
      <p class="contact__role">Co-Founder | Partner</p>
      <ul class="contact__list">
        <li class="contact__item">
          <svg class="contact__icon" viewBox="0 0 16 16" aria-hidden="true"><path d="M2 5c0-2 2-3 6-3s6 1 6 3v1h-3V5H5v1H2zM4 8l2-2h4l2 2v5H4zm4 1.2a1.6 1.6 0 1 0 0 3.2 1.6 1.6 0 0 0 0-3.2z"/></svg>
          +65 555-0147
        </li>
        <li class="contact__item">
          <svg class="contact__icon" viewBox="0 0 16 16" aria-hidden="true"><path d="M1 3h14v10H1zm1.5 1.3v.4L8 8.5l5.5-3.8v-.4z"/></svg>
          peterwalsh@hlp-lend.example
        </li>
        <li class="contact__item">
          <svg class="contact__icon" viewBox="0 0 16 16" aria-hidden="true"><circle cx="8" cy="8" r="6.5"/></svg>
          www.hlp-lend.example
        </li>
        <li class="contact__item">
          <svg class="contact__icon" viewBox="0 0 16 16" aria-hidden="true"><ellipse cx="6" cy="6.5" rx="5.5" ry="4.5"/><ellipse cx="11" cy="10.5" rx="4.5" ry="3.7"/></svg>
          peterwalsh
        </li>
      </ul>
      <address class="contact__address">42 Kelvin Street, Suite 310<br>Singapore 074219</address>
    </div>
  </section>

  <section class="card card--back" aria-label="Card back">
    <div class="wordmark">
      <span class="wordmark__mark"></span>
      Harborline<br>Lending Partners
    </div>
  </section>
</body>
</html>
```